Help me design my in store poster to promote our Loan product!

We need a design for a 2 X 3 poster inside our stores to promote our installment loan product. We are called Dorn's Check Cashing, but offer loans inside our stores. We are open to a new logo for Dorn's Loans, and open to any new exciting colors to stand out in the store. We provide short term monthly installment loans, we have monthly payments from 3 - 12 months. Our loans range from $100 - $1,400 with low interest. We ask for ID, consistent source of income, and credit check. We help build credit, and it is fast and easy. We want it to be simple and clean to get people's attention when they are inside our stores. Please help!

UPDATE: The design will be for a 2 X 7 poster now. Less words.

Font styles to use
Other font styles liked:
• Rounded corners with the font

Requirements
Must have
• Bold colors, the words: loans, cash, $100 - $1,400, monthly payments, credit building, quick.
Nice to have
• A new logo, the Dorn's Check Cashing logo added as reference

UPDATE: If we can add a quick slogan : FAST CASH NOW or HELP IS HERE or YOUR CASH IS HERE or LOANS FOR LIVING or LOANS FOR LIFE

A DORN'S FINANCE LOGO that looks similar to the GALEWING logo I attached.

```html
<!DOCTYPE html>
<html lang="en">
<head>
<meta charset="utf-8">
<title>Dorn's Loans – In-Store Poster</title>
<link href="https://fonts.googleapis.com/css2?family=Montserrat:wght@500;600;700;800;900&display=swap" rel="stylesheet">
<style>
  :root {
    --blue: #1f5fb0;
    --blue-light: #8fb3dd;
    --red: #e02a2a;
    --ink: #333a44;
    --paper: #ffffff;
    --photo-a: #d9dde2;
    --photo-b: #a9b4c0;
  }
  * { box-sizing: border-box; margin: 0; padding: 0; }
  html, body { width: 859px; height: 1200px; overflow: hidden; background: var(--paper); }
  body { font-family: "Montserrat", Arial, sans-serif; color: var(--ink); }

  .poster { position: relative; width: 859px; height: 1200px; overflow: hidden; background: var(--paper); }

  .hero-photo {
    position: absolute; left: 0; top: 0; width: 859px; height: 470px;
    background: linear-gradient(160deg, var(--photo-a) 0%, #c4ccd5 55%, var(--photo-b) 100%);
  }
  .hero-curve { position: absolute; left: 0; top: 330px; width: 859px; height: 170px; }

  .inset-photo {
    position: absolute; left: 585px; top: 345px; width: 210px; height: 210px;
    border-radius: 50%;
    background: radial-gradient(circle at 40% 45%, #d8d2c6 0%, #9aa4ae 70%);
    border: 8px solid var(--paper);
    box-shadow: 0 0 0 6px var(--red);
  }

  .headline { position: absolute; left: 75px; top: 575px; }
  .headline-lead { font-size: 60px; font-weight: 800; color: var(--blue); letter-spacing: 1px; line-height: 1; }
  .headline-main { font-size: 145px; font-weight: 800; color: var(--red); line-height: 1; letter-spacing: 2px; }

  .benefits { position: absolute; left: 75px; top: 790px; width: 740px; display: flex; gap: 40px; }
  .benefit-column { list-style: none; display: flex; flex-direction: column; gap: 22px; }
  .benefit-column--left { width: 330px; }
  .benefit-column--right { width: 370px; }
  .benefit { display: flex; gap: 14px; font-size: 25px; font-weight: 600; line-height: 1.25; color: var(--ink); }
  .benefit-tick { flex: 0 0 24px; width: 24px; height: 24px; margin-top: 4px; }

  .call-pill {
    position: absolute; left: 58px; top: 1074px; height: 44px;
    display: flex; align-items: stretch; border: 3px solid var(--blue); border-radius: 22px; overflow: hidden;
    background: var(--paper);
  }
  .call-label { background: var(--red); color: var(--paper); font-size: 24px; font-weight: 700; padding: 0 12px 0 18px; display: flex; align-items: center; }
  .call-number { color: var(--blue); font-size: 28px; font-weight: 800; padding: 0 18px 0 12px; display: flex; align-items: center; letter-spacing: 0.5px; }

  .brand {
    position: absolute; right: 55px; top: 1066px; height: 60px;
    display: flex; align-items: center; gap: 12px;
  }
  .brand-dot { flex: 0 0 22px; width: 22px; height: 22px; border-radius: 50%; background: var(--red); }
  .brand-name { font-size: 36px; font-weight: 900; color: var(--blue); letter-spacing: 0.5px; white-space: nowrap; }

  .footer-band {
    position: absolute; left: 0; top: 1140px; width: 859px; height: 60px;
    background: var(--blue); border-top: 5px solid var(--red);
    color: var(--paper); font-size: 22px; font-weight: 700; display: flex; align-items: center; padding-left: 60px;
  }
</style>
</head>
<body>
  <main class="poster">
    <div class="hero-photo" role="img" aria-label="Photo of a smiling couple at a desk meeting a loan officer who shakes their hand"></div>

    <svg class="hero-curve" viewBox="0 0 859 170" preserveAspectRatio="none" aria-hidden="true">
      <path d="M0 70 Q430 0 859 40 L859 170 L0 170 Z" fill="var(--blue-light)"/>
      <path d="M0 95 Q430 25 859 60 L859 170 L0 170 Z" fill="var(--blue)"/>
      <path d="M0 110 Q430 45 859 78 L859 170 L0 170 Z" fill="var(--paper)"/>
    </svg>

    <div class="inset-photo" role="img" aria-label="Close-up photo of a hand holding cash banknotes"></div>

    <h1 class="headline">
      <span class="headline-lead">LOOKING FOR</span><br>
      <span class="headline-main">LOAN?</span>
    </h1>

    <div class="benefits">
      <ul class="benefit-column benefit-column--left">
        <li class="benefit"><svg class="benefit-tick" viewBox="0 0 26 26"><circle cx="13" cy="13" r="13" fill="var(--red)"/><path d="M7 13.5l4 4 8-8" stroke="#fff" stroke-width="3" fill="none" stroke-linecap="round" stroke-linejoin="round"/></svg><span>Short term monthly<br>installment loans</span></li>
        <li class="benefit"><svg class="benefit-tick" viewBox="0 0 26 26"><circle cx="13" cy="13" r="13" fill="var(--red)"/><path d="M7 13.5l4 4 8-8" stroke="#fff" stroke-width="3" fill="none" stroke-linecap="round" stroke-linejoin="round"/></svg><span>Monthly payments<br>from 3 - 12 months.</span></li>
        <li class="benefit"><svg class="benefit-tick" viewBox="0 0 26 26"><circle cx="13" cy="13" r="13" fill="var(--red)"/><path d="M7 13.5l4 4 8-8" stroke="#fff" stroke-width="3" fill="none" stroke-linecap="round" stroke-linejoin="round"/></svg><span>Credit building</span></li>
      </ul>
      <ul class="benefit-column benefit-column--right">
        <li class="benefit"><svg class="benefit-tick" viewBox="0 0 26 26"><circle cx="13" cy="13" r="13" fill="var(--red)"/><path d="M7 13.5l4 4 8-8" stroke="#fff" stroke-width="3" fill="none" stroke-linecap="round" stroke-linejoin="round"/></svg><span>Loans range from<br>$100 - $1,400<br>with low interest.</span></li>
        <li class="benefit"><svg class="benefit-tick" viewBox="0 0 26 26"><circle cx="13" cy="13" r="13" fill="var(--red)"/><path d="M7 13.5l4 4 8-8" stroke="#fff" stroke-width="3" fill="none" stroke-linecap="round" stroke-linejoin="round"/></svg><span>Hassel Free</span></li>
        <li class="benefit"><svg class="benefit-tick" viewBox="0 0 26 26"><circle cx="13" cy="13" r="13" fill="var(--red)"/><path d="M7 13.5l4 4 8-8" stroke="#fff" stroke-width="3" fill="none" stroke-linecap="round" stroke-linejoin="round"/></svg><span>Low Cost</span></li>
      </ul>
    </div>

    <div class="call-pill">
      <span class="call-label">CALL</span>
      <span class="call-number">555-014-2600</span>
    </div>

    <div class="brand">
      <span class="brand-dot"></span>
      <span class="brand-name">DORN'S LOANS</span>
    </div>

    <footer class="footer-band">www.dornscheckcashing.com</footer>
  </main>
</body>
</html>
```